Web design for an intellectual property law practice

I need to design a simple landing page that may in the future expand to a full site. It should be very high tech focused.

Target Market(s)

Anyone seeking legal services

Industry/Entity Type

Legal

Number of Pages Required

2 page

Font styles to use
Other font styles liked:
• The same font as my logo

Colors
ec1f27

Requirements
Must have
• My logo (see attached).
Nice to have
• Open to ideas.

```html
<!DOCTYPE html>
<html lang="en">
<head>
<meta charset="utf-8">
<title>Canadian Patent Lawyer – Daniel R. Whitcombe</title>
<link href="https://fonts.googleapis.com/css2?family=Montserrat:wght@300;400;500;600;700&display=swap" rel="stylesheet">
<style>
  :root {
    --red: #ec1f27;
    --charcoal: #2b2a2b;
    --ink: #1f1f1f;
    --muted: #555;
    --hero-bg: #dcd4cf;
    --card-light: #e6e2e1;
    --card-dark: #330407;
    --btn-grey: #d9d6d5;
    --white: #ffffff;
  }
  * { box-sizing: border-box; margin: 0; padding: 0; }
  html, body { width: 678px; height: 1200px; overflow: hidden; background: var(--white); }
  body { font-family: "Montserrat", sans-serif; color: var(--ink); position: relative; }
  .abs { position: absolute; }

  .site-header { position: absolute; left: 0; top: 0; width: 678px; height: 32px; background: var(--charcoal); }
  .header-brand { position: absolute; left: 84px; top: 10px; display: flex; align-items: center; gap: 5px; color: var(--white); font-size: 8px; font-weight: 500; }
  .brand-dot { width: 10px; height: 10px; border-radius: 50%; border: 1px solid #cfcfcf; }
  .header-phone { position: absolute; right: 84px; top: 9px; display: flex; align-items: center; gap: 8px; color: var(--white); font-size: 10px; font-weight: 500; }

  .hero { position: absolute; left: 0; top: 32px; width: 678px; height: 409px; background: var(--hero-bg); }
  .hero-portrait { position: absolute; left: 84px; top: 36px; width: 226px; height: 373px; background: linear-gradient(180deg, #cfc5bf 0%, #8d8580 35%, #2f2f33 70%, #232326 100%); border-radius: 90px 90px 0 0; }
  .hero-brand { position: absolute; left: 346px; top: 150px; width: 200px; display: flex; align-items: center; justify-content: center; gap: 5px; font-size: 11px; font-weight: 500; color: var(--ink); }
  .hero-brand .brand-dot { border-color: var(--ink); width: 12px; height: 12px; }
  .hero-title { position: absolute; left: 339px; top: 238px; font-size: 17px; font-weight: 700; letter-spacing: 0.1px; }
  .hero-title span { color: var(--red); }
  .hero-lead { position: absolute; left: 339px; top: 268px; width: 260px; font-size: 7.6px; line-height: 13px; color: #444; }
  .hero-lead strong { font-weight: 600; }
  .btn { display: inline-flex; align-items: center; justify-content: center; font-family: "Montserrat", sans-serif; text-decoration: none; }
  .btn-contact { position: absolute; left: 339px; top: 336px; width: 107px; height: 30px; background: var(--red); color: var(--white); font-size: 9px; font-weight: 500; }

  .section-title { position: absolute; left: 0; width: 678px; text-align: center; font-size: 13px; font-weight: 500; }
  .about-text { position: absolute; left: 84px; top: 516px; width: 510px; text-align: center; font-size: 7.6px; line-height: 13px; color: #444; }
  .btn-outline { position: absolute; left: 297px; top: 575px; width: 83px; height: 21px; border: 1px solid #888; border-radius: 2px; font-size: 7px; font-weight: 600; color: var(--ink); }

  .card { position: absolute; top: 724px; width: 162px; height: 178px; background: var(--card-light); text-align: center; }
  .card-title { margin-top: 30px; font-size: 9.6px; font-weight: 500; color: var(--ink); }
  .card-text { margin: 16px auto 0; width: 140px; font-size: 6.2px; line-height: 11.6px; color: #666; }
  .card-btn { position: absolute; left: 48px; top: 126px; width: 66px; height: 19px; background: var(--btn-grey); color: var(--ink); font-size: 6.4px; }
  .card.is-active { background: var(--card-dark); }
  .card.is-active .card-title, .card.is-active .card-text { color: var(--white); }
  .card.is-active .card-btn { color: var(--red); }

  .cta-title { position: absolute; left: 0; top: 982px; width: 678px; text-align: center; font-size: 16px; font-weight: 400; }
  .cta-sub { position: absolute; left: 0; top: 1004px; width: 678px; text-align: center; font-size: 6px; color: #666; }
  .btn-phone { position: absolute; left: 217px; top: 1038px; width: 113px; height: 22px; background: var(--red); color: var(--white); font-size: 12px; font-weight: 500; }
  .btn-email { position: absolute; left: 355px; top: 1038px; width: 113px; height: 22px; background: var(--charcoal); color: var(--white); font-size: 8px; font-weight: 600; }
  .gavel-art { position: absolute; left: 548px; top: 1046px; width: 92px; height: 89px; background: linear-gradient(135deg, #111 0%, #000 100%); border-radius: 10px; }

  .site-footer { position: absolute; left: 0; top: 1135px; width: 678px; height: 65px; background: var(--charcoal); }
  .copyright { position: absolute; left: 0; top: 21px; width: 678px; text-align: center; font-size: 6.2px; color: #ddd; }
  .social { position: absolute; left: 303px; top: 38px; display: flex; gap: 5px; }
  .social-dot { width: 16px; height: 16px; border-radius: 50%; background: var(--white); }
</style>
</head>
<body>
  <header class="site-header">
    <div class="header-brand"><span class="brand-dot"></span>northpatentcounsel</div>
    <div class="header-phone">
      <svg width="12" height="12" viewBox="0 0 24 24" fill="none" stroke="#fff" stroke-width="1.6" aria-hidden="true"><path d="M5 3h4l2 5-2.5 1.5a11 11 0 0 0 6 6L16 13l5 2v4a2 2 0 0 1-2 2A17 17 0 0 1 3 5a2 2 0 0 1 2-2z"/></svg>
      (416) 555-0187
    </div>
  </header>

  <section class="hero">
    <div class="hero-portrait" role="img" aria-label="Portrait photograph of the patent lawyer in a dark pinstripe suit and blue tie"></div>
    <div class="hero-brand"><span class="brand-dot"></span>northpatentcounsel</div>
    <h1 class="hero-title">CANADIAN PATENT <span>LAWYER</span></h1>
    <p class="hero-lead"><strong>Daniel R. Whitcombe</strong> is a patent lawyer with expertise in the acquisition, protection &amp; enforcement of intellectual property in Canada. Helping you with your Canadian IP rights.</p>
    <a class="btn btn-contact" href="#contact">Contact Me</a>
  </section>

  <h2 class="section-title" style="top:486px">About Me</h2>
  <p class="about-text">DANIEL R. WHITCOMBE is a partner with HARROW &amp; LISLE in its Toronto Office.&nbsp; Daniel is an intellectual property lawyer with the firm's Technology and Intellectual Property practice groups. Daniel's practice focuses on all aspects of the acquisition, protection, enforcement and strategic use of a wide range of intellectual property assets in Canada and around the world.</p>
  <a class="btn btn-outline" href="#about">Read More</a>

  <h2 class="section-title" style="top:676px">Experience</h2>
  <article class="card is-active" style="left:84px">
    <h3 class="card-title">Patents &amp; Industrial Designs</h3>
    <p class="card-text">As a registered patent agent with the Canadian Patent Registry (CPR), Daniel's practice focuses on the drafting and prosecuting of patent applications in</p>
    <a class="btn card-btn" href="#">Read More</a>
  </article>
  <article class="card" style="left:256px">
    <h3 class="card-title">Patents &amp; Industrial Designs</h3>
    <p class="card-text">As a registered patent agent with the Canadian Patent Registry (CPR), Daniel's practice focuses on the drafting and prosecuting of patent applications in</p>
    <a class="btn card-btn" href="#">Read More</a>
  </article>
  <article class="card" style="left:431px">
    <h3 class="card-title">Patents &amp; Industrial Designs</h3>
    <p class="card-text">As a registered patent agent with the Canadian Patent Registry (CPR), Daniel's practice focuses on the drafting and prosecuting of patent applications in</p>
    <a class="btn card-btn" href="#">Read More</a>
  </article>

  <h2 class="cta-title" id="contact">Canadian Patent Lawyer</h2>
  <p class="cta-sub">Don't hesitate to reach out if you have any questions</p>
  <a class="btn btn-phone" href="#">(416) 555-0187</a>
  <a class="btn btn-email" href="#">SEND ME AN EMAIL</a>
  <div class="gavel-art" role="img" aria-label="Black silhouette illustration of a judge's gavel and sound block"></div>

  <footer class="site-footer">
    <p class="copyright">Copyright © 2018 Daniel R. Whitcombe&nbsp; - All Rights Reserved.</p>
    <div class="social" aria-label="Social links">
      <span class="social-dot"></span><span class="social-dot"></span><span class="social-dot"></span><span class="social-dot"></span>
    </div>
  </footer>
</body>
</html>
```